I have a transportation trucking company and I’m expanding and hiring drivers

I need a flyer for my social media to let people know I’m hiring and looking for drivers , Please incorporate my company logo and i need to flyer to give some information about the position, I will upload some examples,

I do need it to say We are hiring!
We are looking for CDL- Class A Drivers
2 Years Minimum Driving Experience
Percentage Pay
Clean Driving Record
No Violations or accidents
Weekly Direct Deposit
Sign On bonus
Holiday Bonus
Detention/ Layover Pay
Must Stay out a minimum of 2 full weeks

Interested in more information?
Email info@marlowhaulage.com
(415) 286-9031

Marlow Haulage LLC
238 Birch Hollow Lane Suite 150 Ferndale PA 18921

Industry/Entity Type

Long Distance Trucking

Font styles to use
Serif
Sans Serif
Decorative
Script

Requirements
Must have
• Please incorporate my logo into the flyer

Please have just the flyer take up the whole canvas this will be printed and posted on our social media’s
Nice to have

```html
<!DOCTYPE html>
<html lang="en">
<head>
<meta charset="utf-8">
<title>Marlow Haulage LLC – We Are Hiring</title>
<link rel="stylesheet" href="https://fonts.googleapis.com/css2?family=Montserrat:wght@400;500;600;700;800;900&display=swap">
<style>
  :root {
    --ink: #1a1a1b;
    --white: #ffffff;
    --blue: #1f63b8;
    --dot: #1a7fd6;
    --navy: #2d3a6e;
    --navy-soft: rgba(38, 84, 170, 0.72);
    --grey: #9a9ca3;
    --photo-red: #8e2a2c;
    --photo-dark: #2a2426;
    --photo-warm: #d8a17e;
  }
  * { margin: 0; padding: 0; box-sizing: border-box; }
  html, body { width: 855px; height: 1200px; overflow: hidden; background: var(--ink); }
  .flyer {
    position: relative; width: 855px; height: 1200px; overflow: hidden;
    background: var(--ink); font-family: "Montserrat", sans-serif; color: var(--white);
  }
  .hero-photo {
    position: absolute; left: 0; top: 0; width: 855px; height: 584px;
    background:
      radial-gradient(ellipse at 58% 4%, var(--photo-warm) 0%, rgba(216,161,126,0) 38%),
      linear-gradient(160deg, #6b3236 0%, var(--photo-red) 35%, #5a2426 60%, var(--photo-dark) 100%);
  }
  .shapes { position: absolute; left: 0; top: 0; width: 855px; height: 1200px; }
  .headline-top {
    position: absolute; left: 112px; top: 268px;
    font-weight: 800; font-size: 82px; line-height: 1; letter-spacing: 20px;
  }
  .headline-main {
    position: absolute; left: 46px; top: 340px;
    font-weight: 800; font-size: 168px; line-height: 1; letter-spacing: -4px;
  }
  .role-intro {
    position: absolute; left: 59px; top: 660px;
    font-weight: 800; font-size: 26px; letter-spacing: -1px; color: var(--blue);
  }
  .role-title {
    position: absolute; left: 58px; top: 696px;
    font-weight: 800; font-size: 42px; line-height: 46px; letter-spacing: -0.5px;
  }
  .perks {
    position: absolute; left: 440px; top: 660px; list-style: none;
  }
  .perks li {
    position: relative; padding-left: 41px; margin-bottom: 8.5px;
    font-size: 19px; font-weight: 500; line-height: 19.5px; letter-spacing: 1px;
  }
  .perks li::before {
    content: ""; position: absolute; left: 0; top: 3px;
    width: 12px; height: 12px; border-radius: 50%; background: var(--dot);
  }
  .contact-heading {
    position: absolute; left: 479px; top: 1020px;
    font-weight: 800; font-size: 22.5px; line-height: 23px; color: var(--blue); letter-spacing: -0.3px;
  }
  .contact-list {
    position: absolute; left: 479px; top: 1079px;
    font-size: 12.5px; line-height: 17px; font-weight: 600; letter-spacing: 0.4px;
  }
  .contact-list .row { display: flex; }
  .contact-list .label { width: 58px; color: var(--grey); font-weight: 500; }
  .brand {
    position: absolute; left: 40px; top: 990px; width: 272px; text-align: center;
  }
  .brand-square {
    width: 62px; height: 62px; margin: 0 auto 22px; background: var(--white);
  }
  .brand-name {
    font-weight: 700; font-size: 28px; line-height: 32px; color: var(--white); letter-spacing: 1px;
  }
</style>
</head>
<body>
<main class="flyer">
  <div class="hero-photo" role="img" aria-label="Photo of a truck driver with arms crossed standing beside a red semi-truck"></div>

  <svg class="shapes" viewBox="0 0 855 1200" aria-hidden="true">
    <polygon points="769,0 855,0 855,763 595,584 440,584" fill="var(--navy-soft)"/>
    <polygon points="129,874 411,1056 316,1200 0,1200 0,1069" fill="var(--navy)"/>
  </svg>

  <div class="headline-top">WE ARE</div>
  <div class="headline-main">HIRING</div>

  <div class="role-intro">WE ARE LOOKING FOR</div>
  <h1 class="role-title">CDL- CLASS A<br>DRIVERS</h1>

  <ul class="perks">
    <li>2 Years Minimum<br>Driving Experience</li>
    <li>Percentage Pay</li>
    <li>Clean Driving Record</li>
    <li>No Violations or Accidents</li>
    <li>Weekly Direct Deposit</li>
    <li>Sign On Bonus</li>
    <li>Holiday Bonus</li>
    <li>Detention/ Layover Pay</li>
    <li>Must Stay Out a Minimum<br>of 2 Full Weeks</li>
  </ul>

  <div class="brand">
    <div class="brand-square"></div>
    <div class="brand-name">MARLOW HAULAGE<br>LLC</div>
  </div>

  <h2 class="contact-heading">INTERESTED IN MORE<br>INFORMATION?</h2>
  <div class="contact-list">
    <div class="row"><span class="label">Phone</span><span>: (415) 286-9031</span></div>
    <div class="row"><span class="label">Email</span><span>: info@marlowhaulage.com</span></div>
    <div class="row"><span class="label">Address</span><span>: 238 Birch Hollow Lane Suite 150<br>&nbsp;&nbsp;Ferndale PA 18921</span></div>
  </div>
</main>
</body>
</html>
```